Australian Software Consultancy needs new Business Card Design

Design Business Card based on existing design artefacts (attached). We are open to all designs. As its a 2 sided design and we thought it might be quite striking to have one side with a black background and te other side with a white background.

Target Market(s)

Financial Services mainly.

Industry/Entity Type

Business

Contact Information for Business Card

Name :
Position :
Email :

Requirements
Must have
• Funky design using our existing assets

```html
<!DOCTYPE html>
<html lang="en">
<head>
<meta charset="utf-8">
<title>Deep Field — Business Card</title>
<link href="https://fonts.googleapis.com/css2?family=Open+Sans:wght@400;600;700&display=swap" rel="stylesheet">
<style>
  :root {
    --backdrop: #e7e4df;
    --card-white: #ffffff;
    --card-black: #0d0d0d;
    --brand-red: #e2232f;
    --ink: #2a2a2a;
    --ink-soft: #555555;
    --divider: #d6d6d6;
  }
  * { margin: 0; padding: 0; box-sizing: border-box; }
  html, body {
    width: 1200px; height: 1024px; overflow: hidden;
    background: var(--backdrop);
    font-family: "Open Sans", Arial, sans-serif;
  }
  .sheet {
    position: relative; width: 1200px; height: 1024px;
    display: flex; flex-direction: column; align-items: center; justify-content: center; gap: 56px;
  }
  .card {
    position: relative; width: 760px; height: 434px; overflow: hidden;
    box-shadow: 0 6px 18px rgba(0,0,0,0.18);
  }

  /* White side */
  .card--front { background: var(--card-white); }
  .card--front .end-band {
    position: absolute; top: 0; right: 0; width: 92px; height: 100%;
    background: var(--card-black);
  }
  .card--front .edge-band {
    position: absolute; left: 0; bottom: 0; width: calc(100% - 92px); height: 26px;
    background: var(--brand-red);
  }
  .brand-block {
    position: absolute; left: 40px; top: 0; width: 260px; height: calc(100% - 26px);
    display: flex; align-items: center; gap: 14px;
  }
  .brand-dot {
    width: 26px; height: 26px; border-radius: 50%;
    background: var(--brand-red); flex: none;
  }
  .brand-name {
    font-weight: 700; font-size: 34px; color: var(--brand-red);
    letter-spacing: 1px; white-space: nowrap;
  }
  .divider {
    position: absolute; left: 318px; top: 46px; width: 2px; height: 300px;
    background: linear-gradient(to bottom, transparent, var(--divider) 20%, var(--divider) 80%, transparent);
  }
  .contact { position: absolute; left: 348px; top: 58px; color: var(--ink); }
  .contact .person { font-size: 30px; font-weight: 600; color: var(--brand-red); line-height: 1.1; }
  .contact .role { font-size: 20px; color: var(--ink-soft); margin-top: 4px; }
  .contact .address { font-size: 19px; line-height: 1.35; margin-top: 34px; }
  .contact .lines { list-style: none; margin-top: 26px; font-size: 19px; line-height: 1.45; }
  .contact .lines li { display: flex; align-items: center; gap: 10px; }
  .contact .lines svg { width: 16px; height: 16px; flex: none; }

  /* Black side */
  .card--back {
    background: linear-gradient(135deg, #1b1b1b 0%, var(--card-black) 60%);
  }
  .back-brand {
    position: absolute; left: 0; right: 0; top: 160px;
    display: flex; align-items: center; justify-content: center; gap: 20px;
  }
  .back-dot {
    width: 34px; height: 34px; border-radius: 50%;
    background: var(--brand-red); flex: none;
  }
  .back-name {
    font-weight: 700; font-size: 64px; letter-spacing: 3px; color: #ffffff;
    white-space: nowrap;
  }
  .back-url {
    position: absolute; left: 0; right: 0; top: 262px; text-align: center;
    font-size: 18px; color: #ffffff; letter-spacing: 0.5px;
  }
</style>
</head>
<body>
<main class="sheet">
  <section class="card card--front" aria-label="Business card, white side">
    <div class="brand-block">
      <span class="brand-dot"></span>
      <span class="brand-name">DEEP FIELD</span>
    </div>
    <div class="divider"></div>
    <div class="contact">
      <p class="person">Jordan Pike</p>
      <p class="role">Job Title</p>
      <p class="address">210 Harbor Lane<br>Port Elara,<br>Westshire 40172</p>
      <ul class="lines">
        <li>
          <svg viewBox="0 0 16 16"><circle cx="8" cy="8" r="8" fill="var(--brand-red)"/><path d="M5 4.5l1.6-.6 1 2.2-1 .8c.5 1 1.3 1.8 2.3 2.3l.8-1 2.2 1-.6 1.6c-3 .2-6.5-3.3-6.3-6.3z" fill="#fff"/></svg>
          555-014-2273
        </li>
        <li>
          <svg viewBox="0 0 16 16"><circle cx="8" cy="8" r="8" fill="var(--brand-red)"/><rect x="4" y="5" width="8" height="6" fill="none" stroke="#fff" stroke-width="1.2"/><path d="M4 5l4 3.2L12 5" fill="none" stroke="#fff" stroke-width="1.2"/></svg>
          hello@deepfieldco.com
        </li>
        <li>
          <svg viewBox="0 0 16 16"><circle cx="8" cy="8" r="8" fill="var(--brand-red)"/><circle cx="8" cy="8" r="4" fill="none" stroke="#fff" stroke-width="1.1"/><path d="M4 8h8M8 4c-2 2.4-2 5.6 0 8M8 4c2 2.4 2 5.6 0 8" fill="none" stroke="#fff" stroke-width="1"/></svg>
          www.deepfieldco.com
        </li>
      </ul>
    </div>
    <div class="end-band"></div>
    <div class="edge-band"></div>
  </section>

  <section class="card card--back" aria-label="Business card, black side">
    <div class="back-brand">
      <span class="back-dot"></span>
      <p class="back-name">DEEP FIELD</p>
    </div>
    <p class="back-url">www.deepfieldco.com</p>
  </section>
</main>
</body>
</html>
```